Womans Supplement Designs

Launching a Supplement company and need to get some initial designs created, I've attached our logo and the bottle type that I want the samples done one.

This project is for our Whey Protein we are starting with Vanilla, chocolate and strawberry banana

(ALL DESIGN VARIATIONS MUST BE A WHITE BOTTLE NOT BLACK)

(FOR DESIGN SAMPLES PLEASE USE THE SUPPLEMENT BOTTLE STYLE I PROVIDED)

Whoever is selected the winner I will have more work for you to complete the disigns for the rest of the products in the line, Just want to get this shake completed first

Target Market(s)

Women

Requirements
Must have
• Must have our current logo involved

the name of this product will be "KIVA LUM"

Must have this slogan,

ALL-IN-ONE PREMIUM PROTEIN NUTRITIONAL SHAKE FOR BLACK WOMEN

This is our meal replacement

the design should try to keep the same look and feel of the existing provided supplement images

we are starting with chocolate, vanilla and strawberry banana

this is for women and should look colorful and appeal to them
Should not have
• Do not use an image of a person or lady, don't want it branded to a person

```html
<!DOCTYPE html>
<html lang="en">
<head>
<meta charset="utf-8">
<title>Kiva Lum Whey Protein Label – Vanilla</title>
<link rel="stylesheet" href="https://fonts.googleapis.com/css2?family=Archivo+Black&family=Dancing+Script:wght@700&family=Exo+2:ital,wght@0,600;0,700;0,800;1,700;1,800&display=swap">
<style>
  :root {
    --page-bg: #e6e6e6;
    --ink-black: #0b0b0b;
    --paper-white: #ffffff;
    --tan-light: #d6bf9b;
    --tan-deep: #a9834c;
    --accent-pink: #e5195a;
    --silhouette-tone: #1c1916;
    --pod-brown: #3b2416;
    --flower-yellow: #f2d25a;
  }
  html, body {
    margin: 0;
    padding: 0;
    width: 1200px;
    height: 900px;
    overflow: hidden;
    background: var(--page-bg);
  }
  .canvas {
    position: relative;
    width: 1200px;
    height: 900px;
  }
  .label {
    position: absolute;
    left: 100px;
    top: 130px;
    width: 1000px;
    height: 640px;
    overflow: hidden;
    box-shadow: 0 14px 40px rgba(0,0,0,0.18);
  }
  .label svg { display: block; }
  .brand-name {
    font-family: "Exo 2", sans-serif;
    font-weight: 700;
    font-size: 24px;
    letter-spacing: 4px;
    fill: var(--ink-black);
  }
  .product-name {
    font-family: "Archivo Black", sans-serif;
    font-size: 84px;
    fill: var(--accent-pink);
    stroke: var(--paper-white);
    stroke-width: 6px;
    paint-order: stroke;
    letter-spacing: 2px;
  }
  .slogan {
    font-family: "Exo 2", sans-serif;
    font-style: italic;
    font-weight: 800;
    font-size: 18px;
    fill: var(--paper-white);
  }
  .slogan-highlight {
    font-family: "Exo 2", sans-serif;
    font-style: italic;
    font-weight: 800;
    font-size: 18px;
    fill: var(--ink-black);
  }
  .protein-type {
    font-family: "Exo 2", sans-serif;
    font-weight: 800;
    font-size: 12px;
    fill: var(--paper-white);
    letter-spacing: 0.5px;
  }
  .net-weight {
    font-family: "Exo 2", sans-serif;
    font-weight: 600;
    font-size: 24px;
    fill: var(--paper-white);
  }
  .meal-claim {
    font-family: "Exo 2", sans-serif;
    font-weight: 800;
    font-size: 22px;
    fill: var(--paper-white);
    letter-spacing: 0.5px;
  }
  .flavour-name {
    font-family: "Dancing Script", cursive;
    font-weight: 700;
    font-size: 40px;
    fill: var(--paper-white);
  }
</style>
</head>
<body>
<main class="canvas">
  <div class="label">
    <svg width="1000" height="640" viewBox="0 0 1000 640" xmlns="http://www.w3.org/2000/svg">
      <defs>
        <linearGradient id="label-ground" x1="0" y1="0" x2="0" y2="1">
          <stop offset="0" stop-color="var(--paper-white)"/>
          <stop offset="0.2" stop-color="var(--paper-white)"/>
          <stop offset="0.3" stop-color="var(--tan-light)"/>
          <stop offset="1" stop-color="var(--tan-light)"/>
        </linearGradient>
        <linearGradient id="tan-shade" x1="0" y1="0" x2="1" y2="0">
          <stop offset="0" stop-color="var(--tan-deep)" stop-opacity="0.7"/>
          <stop offset="0.35" stop-color="var(--tan-deep)" stop-opacity="0"/>
        </linearGradient>
        <linearGradient id="inner-fade" gradientUnits="userSpaceOnUse" x1="0" y1="0" x2="0" y2="330">
          <stop offset="0" stop-color="var(--paper-white)"/>
          <stop offset="0.4" stop-color="#f0f0f0"/>
          <stop offset="0.85" stop-color="var(--ink-black)"/>
        </linearGradient>
        <linearGradient id="pod-tone" x1="0" y1="0" x2="1" y2="0">
          <stop offset="0" stop-color="var(--pod-brown)"/>
          <stop offset="0.55" stop-color="var(--flower-yellow)"/>
          <stop offset="1" stop-color="var(--pod-brown)"/>
        </linearGradient>
      </defs>

      <!-- ground -->
      <rect class="label-ground" width="1000" height="640" fill="url(#label-ground)"/>
      <rect class="label-ground-shade" y="120" width="1000" height="520" fill="url(#tan-shade)"/>

      <!-- athlete silhouette area -->
      <rect class="athlete-figure" x="0" y="150" width="150" height="490" fill="var(--silhouette-tone)" role="img" aria-label="Silhouette of a woman in a boxing stance"/>

      <!-- V stripes -->
      <polygon class="v-stripe-outer" points="-20,0 1020,0 550,640 450,640" fill="var(--ink-black)"/>
      <polygon class="v-stripe-white" points="40,0 960,0 500,610" fill="var(--paper-white)"/>
      <polygon class="v-stripe-inner" points="90,0 910,0 500,580" fill="var(--ink-black)"/>
      <polygon class="v-core" points="160,0 840,0 500,330" fill="url(#inner-fade)"/>

      <!-- diagonal claim band -->
      <polygon class="claim-gap" points="1020,0 1040,0 570,640 550,640" fill="var(--paper-white)"/>
      <polygon class="claim-band" points="937,140 1007,140 640,640 570,640" fill="var(--accent-pink)"/>
      <text class="meal-claim" x="788" y="398" text-anchor="middle" transform="rotate(-53.7 788 390)">THIS IS OUR MEAL REPLACEMENT</text>

      <!-- brand -->
      <text class="brand-name" x="500" y="92" text-anchor="middle">NOVA CREST NUTRITION</text>

      <!-- product name -->
      <text class="product-name" x="500" y="268" text-anchor="middle">KIVA LUM</text>

      <!-- slogan -->
      <text class="slogan" x="500" y="320" text-anchor="middle">ALL-IN-ONE PREMIUM PROTEIN</text>
      <text class="slogan" x="500" y="345" text-anchor="middle">NUTRITIONAL SHAKE</text>
      <rect class="slogan-box" x="408" y="353" width="184" height="24" fill="var(--paper-white)"/>
      <text class="slogan-highlight" x="500" y="371" text-anchor="middle">FOR BLACK WOMEN</text>

      <!-- protein type tag -->
      <polygon class="protein-tag" points="442,430 562,430 552,452 432,452" fill="none" stroke="var(--paper-white)" stroke-width="1.5"/>
      <text class="protein-type" x="497" y="445" text-anchor="middle">WHEY PROTEIN</text>

      <!-- net weight -->
      <text class="net-weight" x="500" y="630" text-anchor="middle">750g</text>

      <!-- flavour -->
      <text class="flavour-name" x="880" y="552" text-anchor="middle">Vanilla</text>
      <rect class="flavour-art" x="815" y="572" width="130" height="34" rx="17" fill="url(#pod-tone)" role="img" aria-label="Vanilla pods with a yellow vanilla flower"/>
    </svg>
  </div>
</main>
</body>
</html>
```